Geschäftspapiere Campingplatz
Zielgruppe
Campingplatz
Aufgabenstellung
Geschäftspapiere, Briefpapier, Visitenkarte, Briefumschlag und DIN A5 Memoblock farblich und designmäßig am Logo orientiert.
Memoblock sollte sich vom Briefpapier unterscheiden und nicht so viele Daten enthalten.
Website, E-Mail, Telefonnummer, Festnetz, Adresse und Inhaber sollen auf dem Briefpapier erscheinen.
Auf der Visitenkarte soll nur statt Inhaber stehen und zusätzlich die Handynummer, sowie alle anderen Daten.
Die Datensätze sollten sich mit entsprechendem Programm von uns bearbeiten lassen.

```html
<!DOCTYPE html>
<html lang="de">
<head>
<meta charset="utf-8">
<title>Camping Lindenhain – Geschäftspapiere</title>
<link href="https://fonts.googleapis.com/css2?family=Source+Sans+3:wght@400;600;700&display=swap" rel="stylesheet">
<style>
  :root {
    --bg: #f7f7f7;
    --paper: #ffffff;
    --green: #6f9628;
    --green-band: #7f9a4b;
    --gold: #b09a2c;
    --ink: #3a3a3a;
    --muted: #6a6a6a;
    --band-text: #e6ecd8;
    --envelope: #f1f1f1;
  }
  * { margin: 0; padding: 0; box-sizing: border-box; }
  html, body { width: 1200px; height: 1000px; overflow: hidden; background: var(--bg); }
  body { position: relative; font-family: "Source Sans 3", Arial, sans-serif; color: var(--ink); }
  .abs { position: absolute; }
  .brand-name { font-family: "Source Sans 3", Arial, sans-serif; font-weight: 700; color: var(--green); white-space: nowrap; line-height: 1; }
  .brand-name .dot { display: inline-block; border-radius: 50%; background: var(--green); vertical-align: middle; }

  /* Hero brand */
  .hero-brand { left: 85px; top: 118px; width: 435px; text-align: center; font-size: 44px; }
  .hero-brand .dot { width: 18px; height: 18px; margin-right: 10px; }

  /* Letterhead */
  .letterhead { left: 36px; top: 213px; width: 533px; height: 753px; background: var(--paper); box-shadow: 1px 1px 3px rgba(0,0,0,.25); }
  .letterhead .edge-gold { left: 0; top: 0; width: 9px; height: 124px; background: var(--gold); }
  .letterhead .edge-green { left: 0; top: 132px; width: 9px; height: 621px; background: var(--green); }
  .letterhead .fold { left: 9px; width: 16px; height: 1px; background: #555; }
  .letterhead .brand-name { left: 66px; top: 62px; font-size: 18px; }
  .letterhead .brand-name .dot { width: 8px; height: 8px; margin-right: 5px; }
  .letterhead .contact { left: 378px; top: 28px; padding-left: 6px; border-left: 1px solid var(--gold); font-size: 8px; line-height: 1.45; }
  .letterhead .contact .org { color: var(--gold); font-weight: 600; font-size: 10px; }
  .letterhead .contact .org b { color: var(--green); font-weight: 600; }
  .letterhead .contact .gap { height: 12px; }
  .letterhead .contact .lbl { color: var(--green); display: inline-block; width: 31px; }
  .letterhead .sender { left: 67px; top: 139px; font-size: 6.5px; color: var(--muted); font-family: Arial, sans-serif; }
  .letterhead .sender span { margin-right: 8px; }
  .letterhead .footer { top: 717px; font-size: 7.5px; line-height: 1.15; color: var(--muted); }
  .letterhead .divider { top: 717px; width: 1px; height: 24px; background: #444; }

  /* Business card front */
  .card { background: var(--paper); box-shadow: 3px 3px 6px rgba(0,0,0,.35); overflow: hidden; }
  .card-front { left: 721px; top: 89px; width: 348px; height: 226px; }
  .card-front .brand-name { left: 15px; top: 44px; font-size: 13px; }
  .card-front .brand-name .dot { width: 7px; height: 7px; margin-right: 4px; }
  .card-front .bar-top { left: 163px; top: 45px; width: 185px; height: 9px; background: var(--gold); }
  .card-front .band { left: 0; top: 78px; width: 348px; height: 92px; background: var(--green-band); }
  .card-front .item { width: 110px; text-align: center; font-size: 7.5px; line-height: 1.3; color: var(--band-text); }
  .card-front .item svg { display: block; margin: 0 auto 2px; }
  .card-front .bar-bottom { left: 0; top: 193px; width: 217px; height: 9px; background: var(--gold); }
  .card-front .holder { left: 246px; top: 188px; font-size: 15px; color: var(--muted); }

  /* Business card back */
  .card-back { left: 716px; top: 359px; width: 348px; height: 226px; }
  .card-back .brand-name { left: 0; width: 348px; top: 98px; text-align: center; font-size: 27px; }
  .card-back .brand-name .dot { width: 11px; height: 11px; margin-right: 7px; }

  /* Envelope */
  .envelope { left: 604px; top: 612px; width: 560px; height: 351px; }
  .envelope .flap { left: 0; top: 0; }
  .envelope .body { left: 0; top: 65px; width: 560px; height: 286px; background: var(--envelope); border-top: 1px solid #aaa; box-shadow: 1px 2px 3px rgba(0,0,0,.2); }
  .envelope .brand-name { left: 34px; top: 98px; font-size: 15px; }
  .envelope .brand-name .dot { width: 7px; height: 7px; margin-right: 5px; }
  .envelope .sender { left: 34px; top: 144px; font-size: 8.5px; letter-spacing: .6px; color: var(--ink); }
  .envelope .window { left: 39px; top: 218px; width: 223px; height: 90px; border: 1px solid #ddd; border-radius: 10px; background: #fafafa; box-shadow: inset 1px 1px 2px rgba(0,0,0,.12); }
  .envelope .corner { width: 10px; height: 10px; border-color: var(--gold); border-style: solid; border-width: 0; }
  .envelope .band-green { left: 0; top: 341px; width: 416px; height: 10px; background: var(--green); }
  .envelope .band-gold { left: 421px; top: 341px; width: 139px; height: 10px; background: var(--gold); }
</style>
</head>
<body>

  <div class="abs brand-name hero-brand"><span class="dot"></span>Camping Lindenhain</div>

  <!-- Letterhead -->
  <section class="abs letterhead">
    <div class="abs edge-gold"></div>
    <div class="abs edge-green"></div>
    <div class="abs fold" style="top:265px"></div>
    <div class="abs fold" style="top:518px"></div>

    <div class="abs brand-name"><span class="dot"></span>Camping Lindenhain</div>

    <div class="abs contact">
      <div class="org">Camping <b>Lindenhain</b></div>
      <div>Marit Bergholz</div>
      <div class="gap"></div>
      <div>Address here, number</div>
      <div>City, Country</div>
      <div style="margin-top:3px"><span class="lbl">Telefon:</span> 55 555-555-555</div>
      <div><span class="lbl">E-mail:</span> &nbsp;email@yourdomain.com</div>
      <div><span class="lbl">Web:</span> &nbsp;www.yourwebsite.com</div>
    </div>

    <div class="abs sender"><span>Erlenweg 12</span><span>71234 Talheim am Fluss</span></div>

    <div class="abs footer" style="left:79px">Bankverbindung<br>Talbank Mittelland eG<br>Konto 000000000r</div>
    <div class="abs divider" style="left:215px"></div>
    <div class="abs footer" style="left:238px">BLZ: 0000y760000<br>Steurnummer: 000/870000<br>Ust-ID: DE 00008900000</div>
    <div class="abs divider" style="left:357px"></div>
    <div class="abs footer" style="left:381px; top:720px">BIC: ETFUuhYGYGU<br>IBAN: 700007900000</div>
  </section>

  <!-- Business card front -->
  <section class="abs card card-front">
    <div class="abs brand-name"><span class="dot"></span>Camping Lindenhain</div>
    <div class="abs bar-top"></div>
    <div class="abs band">
      <div class="abs item" style="left:-5px; top:27px">
        <svg width="20" height="20" viewBox="0 0 20 20" fill="none" stroke="#e6ecd8" stroke-width="1.2"><circle cx="10" cy="10" r="9"/><path d="M5 10.5 10 6l5 4.5M7 9.5V14h6V9.5"/></svg>
        Address here, number<br>City, Country
      </div>
      <div class="abs item" style="left:115px; top:7px">
        <svg width="20" height="20" viewBox="0 0 20 20" fill="none" stroke="#e6ecd8" stroke-width="1.2"><circle cx="10" cy="10" r="9"/><path d="M7.5 6c-1 1 0 5 4.5 7.5.8.3 1.5-.5 1.5-.8l-1.4-1.2-1 .6c-1-.6-2-1.7-2.4-2.8l.8-.8L8.7 6.2C8.3 5.8 7.9 5.7 7.5 6z"/></svg>
        55 555-555-555
      </div>
      <div class="abs item" style="left:115px; top:44px">
        <svg width="20" height="20" viewBox="0 0 20 20" fill="none" stroke="#e6ecd8" stroke-width="1.2"><circle cx="10" cy="10" r="9"/><rect x="7.5" y="5" width="5" height="10" rx="1"/></svg>
        Ole 55 555-555-555<br>Marit 55 555-555-555
      </div>
      <div class="abs item" style="left:239px; top:7px">
        <svg width="20" height="20" viewBox="0 0 20 20" fill="none" stroke="#e6ecd8" stroke-width="1.2"><circle cx="10" cy="10" r="9"/><rect x="5.5" y="7" width="9" height="6.5"/><path d="M5.5 7 10 11l4.5-4"/></svg>
        email@yourdomain.com
      </div>
      <div class="abs item" style="left:239px; top:55px">
        <svg width="20" height="20" viewBox="0 0 20 20" fill="none" stroke="#e6ecd8" stroke-width="1.2"><circle cx="10" cy="10" r="9"/><circle cx="10" cy="10" r="5"/><path d="M5 10h10M10 5c-2.5 3-2.5 7 0 10M10 5c2.5 3 2.5 7 0 10"/></svg>
        www.yourwebsite.com
      </div>
    </div>
    <div class="abs bar-bottom"></div>
    <div class="abs holder">Fam Bergholz</div>
  </section>

  <!-- Business card back -->
  <section class="abs card card-back">
    <div class="abs brand-name"><span class="dot"></span>Camping Lindenhain</div>
  </section>

  <!-- Envelope -->
  <section class="abs envelope">
    <svg class="abs flap" width="560" height="66" viewBox="0 0 560 66" aria-hidden="true">
      <path d="M0 66 L36 10 Q42 0 55 0 L505 0 Q518 0 526 10 L560 56 L560 66 Z" fill="#f1f1f1"/>
    </svg>
    <div class="abs body"></div>
    <div class="abs brand-name"><span class="dot"></span>Camping Lindenhain</div>
    <div class="abs sender">Address here, number &nbsp; City, Country</div>
    <div class="abs window">
      <div class="abs corner" style="left:12px; top:10px; border-top-width:1px; border-left-width:1px"></div>
      <div class="abs corner" style="right:12px; top:10px; border-top-width:1px; border-right-width:1px"></div>
      <div class="abs corner" style="left:12px; bottom:10px; border-bottom-width:1px; border-left-width:1px"></div>
      <div class="abs corner" style="right:12px; bottom:10px; border-bottom-width:1px; border-right-width:1px"></div>
    </div>
    <div class="abs band-green"></div>
    <div class="abs band-gold"></div>
  </section>

</body>
</html>
```